Private Optometric Practice Needs new Presentation Folders/Stationary

We recently moved our office and are looking to refresh our presentation folders and stationary. I tend to prefer simple, clean designs. We are a full scope optometric practice provide high quality eyewear, custom contact lenses, along with emergency care and treatment for dry eyes. We communicate with a lot of other doctors and want to exude professionalism. I have attached 2 versions of our logo.

Target Market(s)

Familys

Industry/Entity Type

Eyecare

Font styles to use
Sans Serif

Colors
0054AA
0677BA
7BADD7
CADEEF
E8F1F8

Requirements
Nice to have
• Bifold, areas to put information about practice, welcome letter

```html
<!DOCTYPE html>
<html lang="en">
<head>
<meta charset="utf-8">
<title>Halcyon Eyecare – Stationery Set</title>
<link rel="stylesheet" href="https://fonts.googleapis.com/css2?family=Montserrat:wght@400;600&family=Arimo:wght@400;700&display=swap">
<style>
:root{
  --board:#c9c9c9;
  --navy:#071824;
  --sky:#3aa8e0;
  --ink:#333c44;
  --grey:#6f767c;
  --rule:#9aa1a6;
  --paper:#ffffff;
  --fold-grey:#d3d5d7;
}
*{box-sizing:border-box;margin:0;padding:0}
html,body{width:867px;height:1200px;overflow:hidden}
body{background:var(--board);position:relative;font-family:Arimo,Arial,sans-serif;color:var(--ink)}
.piece{position:absolute;background:var(--paper);box-shadow:2px 3px 4px rgba(0,0,0,.35);overflow:hidden}
.band{position:absolute;left:0;right:0;bottom:0;height:5px;background:linear-gradient(115deg,var(--navy) 0 74%,var(--paper) 74% 75%,var(--sky) 75%)}

/* brand lockup */
.brand{position:absolute;display:flex;flex-direction:column;align-items:center;font-family:Montserrat,Arial,sans-serif;font-weight:400;color:var(--navy);line-height:1;font-size:var(--s,12px)}
.brand-dot{width:1.3em;height:1.3em;border-radius:50%;background:var(--sky);margin-bottom:.35em}
.brand-name{letter-spacing:.3em;margin-right:-.3em}
.brand-sub{font-size:.55em;letter-spacing:.7em;margin-right:-.7em;margin-top:.45em}
.brand.on-dark{color:#fff}

.contact{font-size:6px;color:var(--grey);line-height:1.45;white-space:nowrap}
.contact .ico{color:var(--sky);margin-right:2px}
.doctor{font-weight:700;color:var(--sky);font-size:7px;white-space:nowrap}

/* folder cover footer */
.cover-footer{position:absolute;top:339px;font-size:4.2px;line-height:1.3;color:#fff;white-space:nowrap}
.cover-footer .ico{color:var(--sky);margin-right:2px}
.cover-footer.address{right:389px;text-align:right}
.cover-footer.reach{left:133px}
.cover-divider{position:absolute;left:128px;top:338px;width:1px;height:12px;background:#fff}

/* letter */
.letter-head-rule{position:absolute;height:1px;background:var(--rule)}
.letter-body{position:absolute;font-size:4px;line-height:1.35;color:var(--grey)}
.letter-body p{margin-bottom:3.5px}
.letter-body .greet{font-size:5.5px;color:var(--ink);margin-bottom:8px}
.letter-body .sign{font-size:3px;margin-top:8px}
.letter-body .signature{font-size:6px;color:var(--ink);margin:10px 0 0 6px;letter-spacing:-.2px}

/* invoice */
.invoice-title{position:absolute;left:19px;font-weight:700;font-size:17px;color:var(--navy)}
.invoice-meta{position:absolute;left:19px;font-size:5.5px;font-weight:700;color:var(--grey);line-height:1.45}
.invoice-meta b{color:var(--sky)}
.invoice-table{position:absolute;left:25px;width:208px;border-collapse:collapse;font-size:5px;color:var(--ink)}
.invoice-table th{background:var(--sky);color:#fff;font-weight:700;height:13px;text-align:left;padding-left:4px;border:1px solid var(--sky)}
.invoice-table td{height:20.6px;border:1px solid var(--grey);padding-left:5px;font-weight:700}
.invoice-table td.num{font-size:6px}
.invoice-table td.price{font-size:4px}
.invoice-table .sum td{height:17px;font-size:4px;text-align:center;padding:0}
.invoice-table .sum td.blank{border:none}
</style>
</head>
<body>

<!-- business card front -->
<section class="piece" style="left:37px;top:50px;width:219px;height:125px">
  <div class="brand" style="--s:12px;left:120px;top:14px"><span class="brand-dot"></span><span class="brand-name">HALCYON</span><span class="brand-sub">EYECARE</span></div>
  <div class="letter-head-rule" style="left:126px;top:73px;width:81px"></div>
  <div class="doctor" style="position:absolute;left:12px;top:65px">DANIEL WHITMORE, O.D.</div>
  <div class="contact" style="position:absolute;left:12px;top:83px">
    <div><span class="ico">☏</span>555-014-2290</div>
    <div><span class="ico">◍</span>WWW.MYHALCYONEYECARE.COM</div>
    <div style="margin-top:2px">4120 Lakeview Pkwy., Suite B, Millbrook, MI 48000</div>
  </div>
  <div class="band"></div>
</section>

<!-- business card back -->
<section class="piece" style="left:275px;top:50px;width:219px;height:125px;background:var(--navy)">
  <div class="brand on-dark" style="--s:19px;left:49px;top:29px"><span class="brand-name">HALCYON</span><span class="brand-sub">EYECARE</span></div>
</section>

<!-- compliment card -->
<section class="piece" style="left:518px;top:54px;width:316px;height:116px">
  <div class="brand" style="--s:12px;left:20px;top:22px"><span class="brand-dot"></span><span class="brand-name">HALCYON</span><span class="brand-sub">EYECARE</span></div>
  <div style="position:absolute;left:110px;top:22px;width:1px;height:52px;background:var(--rule)"></div>
  <div class="doctor" style="position:absolute;left:122px;top:24px;font-size:12px">DANIEL WHITMORE, O.D.</div>
  <div class="contact" style="position:absolute;left:122px;top:47px;font-size:9px">
    <div><span class="ico">☏</span>555-014-2290</div>
    <div><span class="ico">◍</span>WWW.MYHALCYONEYECARE.COM</div>
  </div>
  <div class="contact" style="position:absolute;left:0;right:0;top:87px;text-align:center;font-size:9.5px">4120 Lakeview Pkwy., Suite B, Millbrook, MI 48000</div>
  <div class="band" style="height:8px"></div>
</section>

<!-- envelope front -->
<section class="piece" style="left:37px;top:200px;width:388px;height:169px">
  <div class="brand" style="--s:10px;left:11px;top:12px"><span class="brand-dot"></span><span class="brand-name">HALCYON</span><span class="brand-sub">EYECARE</span></div>
  <div class="contact" style="position:absolute;left:11px;top:55px;font-size:4.8px;line-height:1.2">4120 Lakeview Pkwy.<br>Suite B, Millbrook, MI 48000</div>
  <div class="band" style="height:6px"></div>
</section>

<!-- envelope back -->
<section class="piece" style="left:444px;top:199px;width:388px;height:168px">
  <svg width="388" height="48" style="position:absolute;left:0;top:0" aria-hidden="true">
    <path d="M0 0H388L380 34Q376 46 362 46H26Q12 46 8 34Z" fill="#071824"/>
  </svg>
  <div style="position:absolute;left:186px;top:14px;width:17px;height:17px;border-radius:50%;background:var(--sky)"></div>
</section>

<!-- letterhead -->
<section class="piece" style="left:34px;top:390px;width:258px;height:365px">
  <div class="brand" style="--s:10px;left:20px;top:12px"><span class="brand-dot"></span><span class="brand-name">HALCYON</span><span class="brand-sub">EYECARE</span></div>
  <div class="contact" style="position:absolute;left:160px;top:25px;font-size:4.2px;line-height:1.35">4120 Lakeview Pkwy.<br>Suite B, Millbrook, MI 48000<br><span class="ico">☏</span>555-014-2290<br><span class="ico">◍</span>WWW.MYHALCYONEYECARE.COM</div>
  <div class="letter-head-rule" style="left:20px;top:52px;width:218px"></div>
  <div class="letter-body" style="left:23px;top:112px;width:212px">
    <p class="greet">Dear Mr. Carter,</p>
    <p>Thank you for choosing our practice for your family's vision care. This letter outlines our services, office hours and what to expect during your first comprehensive eye examination with our team.</p>
    <p>We offer full scope optometric care, including custom contact lens fittings, quality eyewear, emergency visits and treatment for dry eye. Our staff will gladly answer any question you may have.</p>
    <p>Our new office provides convenient parking, accessible entrances and a modern optical gallery. Please arrive ten minutes early to complete any forms and bring your current glasses, lenses and insurance card.</p>
    <p>We look forward to seeing you soon and to caring for your eyes for many years.</p>
    <p class="sign">Sincerely,</p>
    <p class="signature">Mara Ellison</p>
  </div>
  <div class="band"></div>
</section>

<!-- presentation folder outside -->
<section class="piece" style="left:321px;top:390px;width:512px;height:362px">
  <div style="position:absolute;left:0;top:0;width:256px;height:362px;background:var(--navy)"></div>
  <div style="position:absolute;left:256px;top:0;width:256px;height:362px;background:linear-gradient(90deg,var(--fold-grey),#fff 40%)"></div>
  <div class="brand on-dark" style="--s:26px;left:42px;top:160px"><span class="brand-name">HALCYON</span><span class="brand-sub">EYECARE</span></div>
  <div class="brand" style="--s:18px;left:320px;top:20px"><span class="brand-dot"></span><span class="brand-name">HALCYON</span><span class="brand-sub">EYECARE</span></div>
  <div class="cover-footer address">4120 Lakeview Pkwy.<br>Suite B, Millbrook, MI 48000</div>
  <div class="cover-divider"></div>
  <div class="cover-footer reach"><span class="ico">☏</span>555-014-2290<br><span class="ico">◍</span>WWW.MYHALCYONEYECARE.COM</div>
  <div class="band"></div>
</section>

<!-- invoice -->
<section class="piece" style="left:34px;top:772px;width:258px;height:365px">
  <div class="brand" style="--s:10px;left:20px;top:12px"><span class="brand-dot"></span><span class="brand-name">HALCYON</span><span class="brand-sub">EYECARE</span></div>
  <div class="contact" style="position:absolute;left:160px;top:25px;font-size:4.2px;line-height:1.35">4120 Lakeview Pkwy.<br>Suite B, Millbrook, MI 48000<br><span class="ico">☏</span>555-014-2290<br><span class="ico">◍</span>WWW.MYHALCYONEYECARE.COM</div>
  <div class="letter-head-rule" style="left:20px;top:52px;width:218px"></div>
  <div class="invoice-title" style="top:58px">INVOICE</div>
  <div class="invoice-meta" style="top:80px"><b>BANK ACCOUNT:</b> 02345678124<br><b>VAT:</b> 0234567<br><b>DATE:</b> 02.03.2024</div>
  <table class="invoice-table" style="top:117px">
    <tr><th style="width:17px">SL.</th><th style="width:98px">ITEM DESCRIPTION</th><th style="width:30px">PRICE</th><th style="width:30px">QTY.</th><th>TOTAL</th></tr>
    <tr><td class="num">1</td><td></td><td class="price">$00.00</td><td class="num">1</td><td></td></tr>
    <tr><td class="num">2</td><td></td><td class="price">$00.00</td><td class="num">2</td><td></td></tr>
    <tr><td class="num">3</td><td></td><td class="price">$00.00</td><td class="num">1</td><td></td></tr>
    <tr><td class="num">4</td><td></td><td class="price">$00.00</td><td class="num">2</td><td></td></tr>
    <tr><td class="num">5</td><td></td><td class="price">$00.00</td><td class="num">1</td><td></td></tr>
    <tr><td class="num">6</td><td></td><td class="price">$00.00</td><td class="num">1</td><td></td></tr>
    <tr class="sum"><td class="blank" colspan="2"></td><td>SUB TOTAL</td><td colspan="2"></td></tr>
    <tr class="sum"><td class="blank" colspan="2"></td><td>TAX</td><td colspan="2"></td></tr>
    <tr class="sum"><td class="blank" colspan="2"></td><td>TOTAL</td><td colspan="2"></td></tr>
  </table>
  <div class="band"></div>
</section>

<!-- presentation folder inside -->
<section class="piece" style="left:324px;top:772px;width:508px;height:365px">
  <div style="position:absolute;left:0;top:0;width:254px;height:365px;background:linear-gradient(90deg,#fff,#ececee)"></div>
  <div style="position:absolute;left:254px;top:0;width:254px;height:365px;background:linear-gradient(90deg,#c4c6c9,#fff 45%)"></div>
  <div style="position:absolute;left:268px;top:16px;width:226px;height:320px;background:#fff">
    <div class="brand" style="--s:7.5px;left:17px;top:11px"><span class="brand-dot"></span><span class="brand-name">HALCYON</span><span class="brand-sub">EYECARE</span></div>
    <div class="contact" style="position:absolute;left:140px;top:21px;font-size:3.5px;line-height:1.35">4120 Lakeview Pkwy.<br>Suite B, Millbrook, MI 48000<br><span class="ico">☏</span>555-014-2290<br><span class="ico">◍</span>WWW.MYHALCYONEYECARE.COM</div>
    <div class="letter-head-rule" style="left:17px;top:46px;width:192px"></div>
    <div class="letter-body" style="left:20px;top:114px;width:190px;font-size:3.6px">
      <p class="greet" style="font-size:5px">Dear Mr. Carter,</p>
      <p>Thank you for choosing our practice for your family's vision care. This letter outlines our services, office hours and what to expect during your first comprehensive eye examination with our team.</p>
      <p>We offer full scope optometric care, including custom contact lens fittings, quality eyewear, emergency visits and treatment for dry eye. Our staff will gladly answer any question you may have.</p>
      <p>Our new office provides convenient parking, accessible entrances and a modern optical gallery. Please arrive ten minutes early to complete any forms and bring your current glasses, lenses and insurance card.</p>
      <p>We look forward to seeing you soon and to caring for your eyes for many years.</p>
      <p class="sign">Sincerely,</p>
    </div>
  </div>
  <svg width="508" height="132" style="position:absolute;left:0;top:233px" aria-hidden="true">
    <path d="M0 0H225Q238 0 240 14L254 119L254 132H0Z" fill="#071824"/>
    <path d="M508 0H283Q270 0 268 14L254 119L254 132H508Z" fill="#071824"/>
  </svg>
</section>

</body>
</html>
```